Business Card Design Project

This is to go hand in hand with our stationery project.
Target Market(s)
Business Professionals in the Finance, HR and C-Level management arena. They are global companies that run enterprise technology solutions/products.
Mostly Male, mid 30's to 60's.
Industry/Entity Type
Business
Font styles to use
Other font styles liked:
- Calibri
Colors
9bcb3c
000000
1b1b1b
c4c4c4
ffffff
Requirements
Must have
- Logo
Name, title, contact details, address on the front of the card.
ABN and web address need to be on the card, along with our tag line
See | Share | Do
We also require rounded corners and for the card to be landscape please.
Our green is
C98 M0 Y93 K0
Modern, contemporary and must have white space for people to write on.
Nice to have
- Consistent elements with the stationery design.
Should not have
- No 90's waves - We want the feeling of movement but no wavey lines.

```html
<!DOCTYPE html>
<html lang="en">
<head>
<meta charset="utf-8">
<title>Kelvra Business Solutions – Business Cards</title>
<link rel="stylesheet" href="https://fonts.googleapis.com/css2?family=Open+Sans:wght@400;600;700&display=swap">
<style>
  :root {
    --green: #9bcb3c;
    --black: #000000;
    --charcoal: #1b1b1b;
    --silver: #c4c4c4;
    --white: #ffffff;
    --backdrop: #8a8d93;
  }
  * { box-sizing: border-box; margin: 0; padding: 0; }
  html, body { width: 1200px; height: 960px; overflow: hidden; }
  body {
    background: var(--backdrop);
    font-family: "Open Sans", sans-serif;
    position: relative;
  }
  .card {
    position: absolute;
    top: 321px;
    width: 520px;
    height: 318px;
    border-radius: 18px;
    overflow: hidden;
    background: var(--white);
    box-shadow: 0 10px 28px rgba(0,0,0,0.35);
  }
  .card--back { left: 50px; }
  .card--front { left: 630px; }

  /* Brand block */
  .brand {
    display: flex;
    align-items: center;
    gap: 10px;
    color: var(--charcoal);
    font-weight: 700;
    line-height: 1.1;
    white-space: nowrap;
  }
  .brand__dot {
    width: 14px; height: 14px;
    border-radius: 50%;
    background: var(--green);
    flex: none;
  }

  /* Back card */
  .card--back .brand {
    position: absolute;
    left: 0; right: 0; top: 100px;
    justify-content: center;
    font-size: 28px;
  }
  .tagline {
    color: var(--charcoal);
    font-weight: 400;
    white-space: nowrap;
  }
  .tagline__dot {
    display: inline-block;
    width: 6px; height: 6px;
    border-radius: 50%;
    background: var(--green);
    vertical-align: middle;
    margin: 0 6px;
  }
  .card--back .tagline {
    position: absolute;
    left: 0; right: 0; top: 150px;
    text-align: center;
    font-size: 22px;
  }
  .abn {
    position: absolute;
    left: 0; right: 0; top: 188px;
    text-align: center;
    font-size: 13px;
    color: var(--charcoal);
  }

  /* Front card */
  .front__top {
    position: absolute;
    left: 0; top: 0; width: 100%; height: 165px;
    background: var(--white);
  }
  .card--front .brand {
    position: absolute;
    left: 28px; top: 84px;
    font-size: 28px;
  }
  .front__company {
    position: absolute;
    right: 30px; top: 38px;
    text-align: right;
    color: var(--charcoal);
  }
  .front__company-name { font-size: 21px; white-space: nowrap; }
  .front__company .tagline { font-size: 21px; margin-top: 2px; }
  .front__stripe {
    position: absolute;
    left: 0; top: 165px; width: 100%; height: 9px;
    background: var(--green);
  }
  .front__bottom {
    position: absolute;
    left: 0; top: 174px; width: 100%; height: 144px;
    background: linear-gradient(180deg, var(--charcoal), var(--black));
    padding: 14px 28px;
  }
  .person__name {
    color: var(--white);
    font-weight: 700;
    font-size: 19px;
    letter-spacing: 0.5px;
    line-height: 1.1;
  }
  .person__title {
    color: var(--green);
    font-weight: 600;
    font-size: 12px;
    margin-bottom: 7px;
  }
  .contact { list-style: none; }
  .contact__item {
    display: flex;
    align-items: center;
    gap: 8px;
    color: var(--white);
    font-size: 11px;
    line-height: 15px;
    white-space: nowrap;
  }
  .contact__icon { width: 11px; height: 11px; flex: none; fill: var(--green); }
</style>
</head>
<body>

<section class="card card--back" aria-label="Business card back">
  <div class="brand"><span class="brand__dot"></span><span>Kelvra Business Solutions</span></div>
  <p class="tagline">Plan<span class="tagline__dot"></span>Build<span class="tagline__dot"></span>Grow</p>
  <p class="abn">ABN: 12 345678 901</p>
</section>

<section class="card card--front" aria-label="Business card front">
  <div class="front__top">
    <div class="brand"><span class="brand__dot"></span><span>Kelvra</span></div>
    <div class="front__company">
      <p class="front__company-name">Kelvra Business Solutions</p>
      <p class="tagline">Plan<span class="tagline__dot"></span>Build<span class="tagline__dot"></span>Grow</p>
    </div>
  </div>
  <div class="front__stripe"></div>
  <div class="front__bottom">
    <p class="person__name">DANIEL MARSH</p>
    <p class="person__title">Managing Director</p>
    <ul class="contact">
      <li class="contact__item">
        <svg class="contact__icon" viewBox="0 0 12 12"><path d="M2 0h3l1 3-2 1.5a7 7 0 0 0 3.5 3.5L9 6l3 1v3a2 2 0 0 1-2 2A10 10 0 0 1 0 2a2 2 0 0 1 2-2z"/></svg>
        +61 2 5550 1842
      </li>
      <li class="contact__item">
        <svg class="contact__icon" viewBox="0 0 12 12"><rect x="3" y="0" width="6" height="3"/><rect x="0" y="4" width="12" height="5" rx="1"/><rect x="3" y="8" width="6" height="4"/></svg>
        +61 2 55503967
      </li>
      <li class="contact__item">
        <svg class="contact__icon" viewBox="0 0 12 12"><path d="M0 2h12v8H0z M1 3l5 4 5-4" fill="var(--green)" stroke="var(--black)" stroke-width="1"/></svg>
        sales@kelvrabusiness.com
      </li>
      <li class="contact__item">
        <svg class="contact__icon" viewBox="0 0 12 12"><circle cx="6" cy="6" r="5.5"/><path d="M0.5 6h11M6 0.5c-3 3-3 8 0 11M6 0.5c3 3 3 8 0 11" stroke="var(--black)" stroke-width="0.8" fill="none"/></svg>
        www.kelvrabusiness.com
      </li>
      <li class="contact__item">
        <svg class="contact__icon" viewBox="0 0 12 12"><path d="M6 0a4 4 0 0 1 4 4c0 3-4 8-4 8S2 7 2 4a4 4 0 0 1 4-4z"/><circle cx="6" cy="4" r="1.5" fill="var(--black)"/></svg>
        Level 7, 42 Harbour Lane, Eastbrook, NSW 2999
      </li>
    </ul>
  </div>
</section>

</body>
</html>
```